Business Card Design

Business Card for professional consulting firm working with large financial institutions.

Target Market(s)

Executive buyers

Industry/Entity Type

Banking

Contact Information for Business Card

Mild creativity wanted. Not boring, but do elaborate artwork.

Font styles to use
Serif
Sans Serif

Colors

Designer to choose colors to be used in the design.

Requirements
Must have
• Standard business card features - company name, individual name, telephone, website, email, locations.
Nice to have
• Two colors
Should not have
• too many colors, fancy printing, cartoons.

```html
<!DOCTYPE html>
<html lang="en">
<head>
<meta charset="utf-8">
<title>Corvane Advisory – Business Card</title>
<link href="https://fonts.googleapis.com/css2?family=Lato:wght@300;400;700&display=swap" rel="stylesheet">
<style>
  :root {
    --stage: #3b3c3e;
    --card-light: #e6e7e7;
    --card-white: #ffffff;
    --ink: #2b2b2b;
    --ink-soft: #5e5e5e;
    --tab-grey: #8c8c8c;
    --photo-dark: #3e3e40;
    --photo-mid: #6a6a6c;
    --accent-grey: #a9adb0;
    --icon-grey: #8a8a8a;
  }
  * { margin: 0; padding: 0; box-sizing: border-box; }
  html, body { width: 1200px; height: 1200px; overflow: hidden; }
  body {
    background: var(--stage);
    font-family: 'Lato', sans-serif;
    display: flex; flex-direction: column; align-items: center;
    justify-content: center; gap: 48px;
  }
  .card {
    width: 900px; height: 514px; border-radius: 34px;
    position: relative; overflow: hidden;
  }
  /* Back side */
  .card-back { background: var(--card-light); }
  .card-back .world-map {
    position: absolute; left: 90px; top: 60px; width: 720px; height: 400px;
    border-radius: 50%;
    background: radial-gradient(ellipse at center, rgba(200,202,203,.55), rgba(230,231,231,0) 70%);
  }
  .card-back .brand {
    position: absolute; left: 0; right: 0; top: 190px;
    display: flex; align-items: center; justify-content: center; gap: 18px;
  }
  .brand-dot { width: 20px; height: 20px; border-radius: 50%; background: var(--accent-grey); flex: none; }
  .brand-name { font-weight: 400; color: var(--ink); letter-spacing: .5px; white-space: nowrap; }
  .card-back .brand-name { font-size: 56px; }
  .tagline {
    position: absolute; left: 0; right: 0; top: 330px; text-align: center;
    font-size: 20px; letter-spacing: 1.5px; color: var(--ink);
  }
  /* Front side */
  .card-front { background: var(--card-white); }
  .card-front svg.artwork { position: absolute; inset: 0; }
  .address {
    position: absolute; left: 150px; width: 470px; top: 270px;
    text-align: center; color: #fff; font-size: 20px; line-height: 1.3; letter-spacing: .3px;
  }
  .front-brand {
    position: absolute; left: 46px; top: 414px;
    display: flex; align-items: center; gap: 12px;
  }
  .front-brand .brand-dot { width: 14px; height: 14px; }
  .front-brand .brand-name { font-size: 28px; }
  .person { position: absolute; left: 340px; top: 370px; }
  .person-name { font-size: 34px; color: var(--ink); font-weight: 300; white-space: nowrap; }
  .person-name strong { font-weight: 700; }
  .person-title { font-size: 20px; color: var(--ink-soft); margin-top: 4px; }
  .divider { position: absolute; left: 585px; top: 350px; width: 2px; height: 110px; background: #9a9a9a; }
  .contacts { position: absolute; left: 608px; top: 342px; list-style: none; }
  .contacts li { display: flex; align-items: center; gap: 12px; height: 40px; font-size: 18px; color: var(--ink); white-space: nowrap; }
  .contact-icon { width: 26px; height: 26px; border-radius: 50%; background: var(--icon-grey); display: flex; align-items: center; justify-content: center; flex: none; }
</style>
</head>
<body>

<section class="card card-back" aria-label="Business card back">
  <div class="world-map" role="img" aria-label="Faint world map in the background"></div>
  <div class="brand">
    <span class="brand-dot"></span>
    <span class="brand-name">Corvane Advisory</span>
  </div>
  <p class="tagline">STRATEGY | INSIGHT | EXECUTION</p>
</section>

<section class="card card-front" aria-label="Business card front">
  <svg class="artwork" width="900" height="514" viewBox="0 0 900 514">
    <defs>
      <linearGradient id="skyline" x1="0" y1="0" x2="1" y2="1">
        <stop offset="0" stop-color="#6a6a6c"/>
        <stop offset="1" stop-color="#3e3e40"/>
      </linearGradient>
    </defs>
    <rect role="img" aria-label="Black and white city skyline photograph"
          x="0" y="0" width="900" height="280" fill="url(#skyline)"/>
    <polygon points="130,258 640,258 606,330 164,330" fill="#8c8c8c"/>
  </svg>
  <p class="address">48 West Harbor Street Meridian Plaza<br>12th Floor Lakeview, Oregon 97630</p>

  <div class="front-brand">
    <span class="brand-dot"></span>
    <span class="brand-name">Corvane Advisory</span>
  </div>

  <div class="person">
    <p class="person-name"><strong>Daniel</strong> Hart</p>
    <p class="person-title">Managing Director</p>
  </div>

  <div class="divider"></div>

  <ul class="contacts">
    <li><span class="contact-icon"><svg width="14" height="14" viewBox="0 0 24 24"><path fill="#fff" d="M6.6 10.8a15 15 0 006.6 6.6l2.2-2.2a1 1 0 011-.25 11.4 11.4 0 003.6.6 1 1 0 011 1V20a1 1 0 01-1 1A17 17 0 013 4a1 1 0 011-1h3.5a1 1 0 011 1c0 1.25.2 2.45.6 3.6a1 1 0 01-.25 1z"/></svg></span>555-014-2287</li>
    <li><span class="contact-icon"><svg width="14" height="14" viewBox="0 0 24 24"><rect x="2" y="5" width="20" height="14" fill="#fff"/><path d="M2 5l10 8 10-8" fill="none" stroke="#8a8a8a" stroke-width="2"/></svg></span>info@corvaneadvisory.com</li>
    <li><span class="contact-icon"><svg width="14" height="14" viewBox="0 0 24 24"><rect x="3" y="4" width="18" height="12" fill="none" stroke="#fff" stroke-width="2.5"/><path d="M9 20h6M12 16v4" stroke="#fff" stroke-width="2.5"/></svg></span>www.corvaneadvisory.com</li>
  </ul>
</section>

</body>
</html>
```